10周年ということで11月に新聞折込を予定しています。
求人の問い合わせも期待していますのである程度は目立つようにしたいのですがあくまでもオープン10周年がメインなのでバランス良くお願いします。
一目見ただけでハナミズキモールの中にある整体院とわかるようにお願いします。
添付しました。
B4
片面
色々とアクセントを加えたいですが基本はグリーン系でお願いします。
添付画像は必要に応じて使用してください。

インサツドウにそのまま出せるように納品して頂くと助かります。

ハナミズキモール内にある整体院です。ぜひホームページをご覧下さい。
http://kt.hogushidou-example.com/
記載項目の添付資料です
画像の添付するとエラーになるので時間が掛かりそうです。
添付です。
なぜか添付すると投稿出来きません。
「記載項目」以外は前回と同じなので下記アドレスからお願いします。
http://www.kobosite-example.jp/work/detail/582617
添付が出来なかった画像につきましてはほとんどがホームページ内の画像なので必要に応じてホームページから使用してください。

コンペ画像②のQRコードは間違えて添付したので使用は避けてください。
記念品ですが、3つの予定が4つに変更になりました。
可能な限り、画像を載せて欲しいと思います。
画像につきましては以下サイトをご使用下さい。
尚、画像の使用は許可を取っておりますので問題ありません。

ことのは帖 メガネ拭きクロス 4枚組
http://store.kaimono-example.jp/momijiten/j-61842.html#ItemInfo

アニマル裁縫セット
http://store.kaimono-example.jp/momijiten/r-0917004.html#ItemInfo

小さくたためるエコトートバッグ
http://store.kaimono-example.jp/momijiten/r-0342807.html#ItemInfo

どうぶつ柄ハンドタオル
http://store.kaimono-example.jp/momijiten/r-0768305.html#ItemInfo

※個数につきましては記載しないで「なくなり次第、終了とさせて頂きます。」という感じでお願いします。

ご提案者様のデザインはレベルが高いのが多く、大分迷いました。
まずは始めに提案した条件に満たさなかった内容は全て却下しました。
最終的には当方スタッフ全員でランキングを付けて一番評価が良かった方を選びました。

この度はご提案頂き、ありがとうございました。
特に厳選中にも関わらず、修正依頼を快く引き受けて頂いた方には感謝いたします。
ご当選されなかった方もこれに懲りずに機会がありましたらまたご提案頂けましたら幸いです。

```html
<!DOCTYPE html>
<html lang="ja">
<head>
<meta charset="utf-8">
<title>ほぐし堂ケアサポート オープン10周年</title>
<link href="https://fonts.googleapis.com/css2?family=Noto+Sans+JP:wght@400;500;700;900&family=Noto+Serif+JP:wght@700;900&display=swap" rel="stylesheet">
<style>
:root{
  --green:#4f9a2c;
  --green-dark:#2f6e1a;
  --green-light:#e6f1d3;
  --green-pale:#f3f8ea;
  --gold:#c79a3c;
  --pink:#e0567f;
  --red:#e23b2e;
  --ink:#333;
  --paper:#fff;
}
*{margin:0;padding:0;box-sizing:border-box}
html,body{width:851px;height:1200px;overflow:hidden;background:var(--paper)}
body{font-family:"Noto Sans JP",sans-serif;color:var(--ink)}
.flyer{position:relative;width:851px;height:1200px;overflow:hidden;background:var(--paper)}

/* header */
.hero{position:absolute;left:0;top:0;width:851px;height:285px;background:linear-gradient(180deg,#fff 0%,var(--green-pale) 100%)}
.hero-band{position:absolute;left:0;top:0;width:851px;height:12px;background:var(--green)}
.brand{position:absolute;left:22px;top:26px;display:flex;align-items:center;gap:6px}
.brand-dot{width:22px;height:22px;border-radius:50%;background:var(--green)}
.brand-name{font-size:13px;font-weight:700;color:var(--green-dark)}
.tagline{position:absolute;left:0;width:100%;top:22px;text-align:center;font-family:"Noto Serif JP",serif;font-weight:900;font-size:40px;line-height:1.4;color:var(--green-dark);letter-spacing:4px}
.lead{position:absolute;left:0;width:100%;top:80px;text-align:center;font-size:15px;font-weight:700;color:var(--green)}
.headline{position:absolute;left:0;width:100%;top:98px;text-align:center;font-family:"Noto Serif JP",serif;font-weight:900;font-size:72px;line-height:1.4;color:var(--green-dark);letter-spacing:2px}
.anniv{position:absolute;left:0;width:100%;top:178px;text-align:center;font-family:"Noto Serif JP",serif;font-weight:900;color:var(--gold);line-height:1}
.anniv .num{font-size:100px;font-style:italic}
.anniv .unit{font-size:52px}

/* columns */
.col{position:absolute;top:292px}
.col-left{left:18px;width:400px}
.col-right{left:432px;width:400px}
.sec-title{background:var(--green);color:#fff;font-weight:900;font-size:18px;line-height:1.4;padding:3px 12px;letter-spacing:4px;border-radius:3px}
.price-list{list-style:none;padding:3px 6px}
.price-list li{display:flex;justify-content:space-between;font-size:15px;line-height:1.5;font-weight:700;padding:3px 0;border-bottom:1px dotted #9bbf84}
.option{display:flex;gap:8px;align-items:center;font-size:14px;font-weight:700;padding:3px 6px 5px}
.option-tag{background:var(--gold);color:#fff;font-size:11px;padding:1px 6px;border-radius:8px}
.fix{display:flex;gap:8px;padding:5px 4px;border-bottom:1px dotted #9bbf84}
.fix-text{flex:1;font-size:10px;line-height:1.5;color:#555}
.fix-text b{display:flex;justify-content:space-between;font-size:15px;color:var(--ink)}
.photo{flex:none;width:92px;height:56px;border-radius:4px;background:linear-gradient(135deg,#d9c3b0,#f1e4d8)}

.access{margin-top:8px;display:flex;gap:8px;height:128px}
.map{width:190px;background:linear-gradient(135deg,#eef3e6,#d7e6c4);border:1px solid #b8cfa3;border-radius:4px}
.access-info{flex:1;font-size:11px;line-height:1.5}
.access-info .shop{font-size:15px;font-weight:900;color:var(--green-dark)}
.hours{margin:3px 0;border:1px solid var(--green);border-radius:4px;padding:2px 6px}
.hours b{color:var(--green)}
.tel{margin-top:8px;display:flex;align-items:center;gap:10px}
.tel-badge{background:var(--pink);color:#fff;font-weight:900;font-size:13px;line-height:1.2;padding:8px 9px;border-radius:50%;text-align:center}
.tel-num{display:flex;align-items:center;gap:6px;font-size:38px;line-height:1.2;font-weight:900;color:var(--green-dark);letter-spacing:1px}

.discount{display:flex;align-items:center;gap:6px;padding:5px 6px;background:var(--green-light);border-radius:4px;margin:4px 0;font-size:11px;font-weight:700}
.discount-tag{background:var(--pink);color:#fff;padding:2px 6px;border-radius:3px;font-size:11px}
.discount-big{color:var(--red);font-size:21px;line-height:1.3;font-weight:900;white-space:nowrap}
.slim-grid{display:grid;grid-template-columns:1fr 1fr;gap:0 16px;padding:0 6px}
.slim-grid span{display:flex;justify-content:space-between;font-size:14px;line-height:1.5;font-weight:700;padding:3px 0;border-bottom:1px dotted #9bbf84}

.recruit{margin-top:8px;border:2px solid var(--green);border-radius:6px;background:var(--green-pale);padding:0 0 8px}
.recruit .sec-title{border-radius:3px 3px 0 0;text-align:center}
.recruit p{font-size:12px;line-height:1.7;padding:8px 12px 0}
.recruit dl{display:grid;grid-template-columns:70px 1fr;font-size:12px;line-height:1.7;padding:6px 12px 0}
.recruit dt{font-weight:700;color:var(--green-dark)}

/* gifts */
.gifts{position:absolute;left:0;top:945px;width:851px;height:255px;background:var(--green-light)}
.gifts-title{position:absolute;left:18px;top:8px;font-size:22px;line-height:1.4;font-weight:900;color:var(--green-dark)}
.gifts-title em{font-style:normal;color:var(--pink)}
.gifts-note{position:absolute;right:18px;top:16px;font-size:12px;font-weight:700;color:var(--ink)}
.gift-row{position:absolute;left:18px;top:46px;width:815px;display:flex;gap:12px}
.gift{flex:1;background:#fff;border-radius:6px;padding:6px;text-align:center}
.gift-label{display:inline-block;background:var(--gold);color:#fff;font-size:11px;font-weight:700;padding:1px 8px;border-radius:8px}
.gift-photo{margin-top:5px;height:115px;border-radius:4px}
.gift-name{margin-top:5px;font-size:11px;font-weight:700;line-height:1.4}
</style>
</head>
<body>
<div class="flyer">

  <header class="hero">
    <div class="hero-band"></div>
    <div class="brand"><span class="brand-dot"></span><span class="brand-name">ほぐし堂</span></div>
    <p class="tagline">身体と心のトータルケア</p>
    <p class="lead">肩のコリから心身のリラックスまで全力でサポート致します</p>
    <h1 class="headline">おかげ様でオープン</h1>
    <p class="anniv"><span class="num">10</span><span class="unit">周年</span></p>
  </header>

  <section class="col col-left">
    <h2 class="sec-title">整　体</h2>
    <ul class="price-list">
      <li><span>60分(基本コース)</span><span>6,300円</span></li>
      <li><span>40分(部分的な調整)</span><span>4,200円</span></li>
      <li><span>80分(ロングコース)</span><span>8,400円</span></li>
      <li><span>120分(ロングコース)</span><span>10,500円</span></li>
    </ul>
    <div class="option"><span class="option-tag">オプション</span>ヘッドセラピー　＋1,050円</div>

    <h2 class="sec-title">部分矯正</h2>
    <div class="fix">
      <div class="fix-text"><b><span>O脚矯正</span><span>5,250円</span></b>脚のゆがみを整え、すっきりとした脚線へ導きます。</div>
      <div class="photo" role="img" aria-label="O脚矯正の施術写真"></div>
    </div>
    <div class="fix">
      <div class="fix-text"><b><span>骨盤矯正</span><span>5,250円</span></b>骨盤のバランスを整え、姿勢と体調を改善します。</div>
      <div class="photo" role="img" aria-label="骨盤矯正の施術写真"></div>
    </div>
    <div class="fix">
      <div class="fix-text"><b><span>骨盤ダイエット</span><span>5,250円</span></b>骨盤から整えて、太りにくい身体づくりを。</div>
      <div class="photo" role="img" aria-label="骨盤ダイエットの施術写真"></div>
    </div>

    <div class="access">
      <div class="map" role="img" aria-label="ハナミズキモール周辺のアクセスマップ"></div>
      <div class="access-info">
        <p class="shop">ほぐし堂ケアサポート</p>
        <p>ハナミズキモール 1F<br>〒000-0000 緑ヶ丘町1-2-3</p>
        <div class="hours"><b>受付時間</b><br>10:00〜20:00<br>年中無休（モール休館日を除く）</div>
        <p>kt.hogushidou-example.com</p>
      </div>
    </div>
    <div class="tel">
      <span class="tel-badge">予約<br>優先</span>
      <span class="tel-num">
        <svg width="32" height="32" viewBox="0 0 24 24" aria-hidden="true"><path fill="#2f6e1a" d="M6.6 10.8c1.4 2.8 3.8 5.1 6.6 6.6l2.2-2.2c.3-.3.7-.4 1-.2 1.1.4 2.3.6 3.6.6.6 0 1 .4 1 1V20c0 .6-.4 1-1 1C10.6 21 3 13.4 3 4c0-.6.4-1 1-1h3.5c.6 0 1 .4 1 1 0 1.3.2 2.5.6 3.6.1.3 0 .7-.2 1z"/></svg>
        0280-00-4821
      </span>
    </div>
  </section>

  <section class="col col-right">
    <h2 class="sec-title">リラクゼーション</h2>
    <ul class="price-list">
      <li><span>20分</span><span>2,100円〜</span></li>
    </ul>

    <h2 class="sec-title">リンパドレナージュ・部分痩せ</h2>
    <ul class="price-list">
      <li><span>リンパドレナージュ</span><span>5,250円</span></li>
    </ul>
    <div class="discount"><span class="discount-tag">セット</span>整体・部分矯正との組み合わせで<span class="discount-big">30％引き！</span></div>
    <div class="slim-grid">
      <span><i>二の腕</i>5,250円</span>
      <span><i>お腹</i>5,250円</span>
      <span><i>ウエスト</i>5,250円</span>
      <span><i>太もも</i>5,250円</span>
      <span><i>ふくらはぎ</i>5,250円</span>
      <span><i>お尻</i>5,250円</span>
    </div>
    <div class="discount"><span class="discount-tag">セット</span>部分痩せ2ヶ所以上の組み合わせで<span class="discount-big">30％引き！</span></div>

    <div class="recruit">
      <h2 class="sec-title">求人情報</h2>
      <p>当院のスタッフとして一緒に働いてくれる方を募集しています。未経験の方も丁寧に指導しますので、お気軽にお問い合わせください。</p>
      <dl>
        <dt>職種</dt><dd>整体師・セラピスト</dd>
        <dt>資格</dt><dd>未経験可・経験者優遇</dd>
        <dt>時間</dt><dd>10:00〜20:00（シフト制）</dd>
        <dt>給与</dt><dd>経験・能力により優遇</dd>
        <dt>待遇</dt><dd>交通費支給・研修制度あり</dd>
        <dt>応募</dt><dd>まずはお電話ください</dd>
      </dl>
    </div>
  </section>

  <section class="gifts">
    <h2 class="gifts-title"><em>10周年</em>記念品プレゼント</h2>
    <p class="gifts-note">※なくなり次第、終了とさせて頂きます。</p>
    <div class="gift-row">
      <div class="gift"><span class="gift-label">記念品①</span><div class="gift-photo" role="img" aria-label="メガネ拭きクロス4枚組の商品写真" style="background:linear-gradient(135deg,#f3d6de,#f9eef1)"></div><p class="gift-name">ことのは帖<br>メガネ拭きクロス 4枚組</p></div>
      <div class="gift"><span class="gift-label">記念品②</span><div class="gift-photo" role="img" aria-label="アニマル裁縫セットの商品写真" style="background:linear-gradient(135deg,#e8d9b8,#f6efdf)"></div><p class="gift-name">アニマル<br>裁縫セット</p></div>
      <div class="gift"><span class="gift-label">記念品③</span><div class="gift-photo" role="img" aria-label="小さくたためるエコトートバッグの商品写真" style="background:linear-gradient(135deg,#cfe2c0,#eef5e6)"></div><p class="gift-name">小さくたためる<br>エコトートバッグ</p></div>
      <div class="gift"><span class="gift-label">記念品④</span><div class="gift-photo" role="img" aria-label="どうぶつ柄ハンドタオルの商品写真" style="background:linear-gradient(135deg,#d6e3f0,#f0f5fa)"></div><p class="gift-name">どうぶつ柄<br>ハンドタオル</p></div>
    </div>
  </section>

</div>
</body>
</html>
```